Membership Sales Page Web Design

We need a website designed to showcase the benefits of joining our online community of technology procurement professionals.

Our community has been around for a while and it's time for a refresh. Included in the brief is Verson 1.0 of the site. You can see the current version of the site @ brivolnet.com.

As part of the refresh, we've acquired a new primary domain name (brivol.com) and will be rolling out both a free and paid subscription model.

Because of this, there should be a strong call to sign (join now) infused within the site.

We would like to see site designs that are clean, flat and minimalistic in nature. Our membership colors are royal blue, grey, and white.

The final design should communicate networking and professional growth.

I'd be particularly interestedin seeing some flat website designs with a strong call to action. Here are some great examples for inspiration:

https://plintora.example/
https://vemmit.example/

Target Market(s)

zenthar 300 companies

Number of Pages Required

1 page

Font styles to use
Sans Serif

Colors
0293ce
3276b5
ffffff

Requirements
Must have
• clean, minimalistic, fee
strong call to action
showcase our different membership levels
highlight the benefits of membership
Nice to have
• n/a
Should not have
• n/a

```html
<!DOCTYPE html>
<html lang="en">
<head>
<meta charset="utf-8">
<title>BRIVOL – Technology Acquisition Professionals</title>
<link href="https://fonts.googleapis.com/css2?family=Open+Sans:wght@400;600;700&family=Roboto:ital,wght@0,400;0,500;0,700;1,400&display=swap" rel="stylesheet">
<style>
:root{
  --blue:#237fb6;
  --blue-dark:#1f6fa3;
  --blue-light:#b9d7ec;
  --bg:#f7f9fb;
  --band:#eef0f3;
  --card:#eef2f6;
  --tier:#dce2e9;
  --ink:#2b2f33;
  --muted:#555b61;
  --white:#ffffff;
  --photo-a:#b9b4ad;
  --photo-b:#8a7c70;
}
*{box-sizing:border-box;margin:0;padding:0}
html,body{width:1200px;height:2898px;overflow:hidden}
body{position:relative;background:var(--bg);font-family:'Roboto',sans-serif;color:var(--ink)}
.abs{position:absolute}
.brand{display:flex;align-items:center;gap:8px;color:var(--blue);font-family:'Roboto',sans-serif;font-weight:700}
.brand .dot{width:14px;height:14px;background:var(--blue);border-radius:50%}
.brand-sub{font-size:11px;color:var(--ink);font-weight:400;font-family:'Roboto',sans-serif}
.nav{left:427px;top:70px;display:flex;gap:26px;font-size:15px;color:#3a3f44}
.nav a{color:inherit;text-decoration:none;position:relative}
.nav a.active::after{content:"";position:absolute;left:5px;right:5px;bottom:-8px;height:2px;background:var(--blue)}
.member-btn{left:1034px;top:64px;width:119px;height:33px;background:var(--blue-light);color:var(--blue);font-size:15px;display:flex;align-items:center;justify-content:center;border-radius:2px}
.hero-title{left:145px;top:150px;width:520px;font-family:'Open Sans',sans-serif;font-weight:700;font-size:42px;line-height:50px;color:var(--blue)}
.hero-text{left:146px;top:320px;width:440px;font-size:18px;line-height:28px;color:#3a3f44;font-weight:300}
.join-label{left:677px;top:148px;width:384px;text-align:center;font-size:13px;letter-spacing:2px;font-weight:500}
.join-form{left:677px;top:174px;width:384px;border:1px solid #d5dade;background:var(--white)}
.field{height:50px;border-bottom:1px solid #e1e5e8;padding:0 16px;display:flex;align-items:center;justify-content:space-between;font-size:15px;color:#5c6268}
.submit{height:50px;background:var(--blue);color:var(--white);display:flex;align-items:center;justify-content:center;font-size:15px;font-weight:500;gap:8px}
.terms{left:677px;top:390px;width:384px;text-align:center;font-size:11px;color:#777}
.terms span{color:var(--blue)}
.band{left:0;top:453px;width:1200px;height:194px;background:var(--band)}
.h2{font-family:'Open Sans',sans-serif;font-size:35px;font-weight:600;color:var(--ink);position:absolute}
.h2 .mark{position:absolute;height:10px;background:var(--blue-light);opacity:.85;bottom:6px;z-index:-1}
.what-text{left:534px;top:486px;width:480px;font-size:13px;line-height:20px;font-weight:500;color:#333}
.what-text em{display:block;margin-top:20px}
.mission-lead{left:147px;top:790px;width:420px;font-family:'Open Sans',sans-serif;font-size:15.5px;line-height:24px;font-weight:600}
.mission-text{left:147px;top:861px;width:460px;font-family:'Open Sans',sans-serif;font-size:13.5px;line-height:23.5px;color:#333}
.photo{position:absolute;border-radius:4px;background:linear-gradient(160deg,var(--photo-a),var(--photo-b))}
.why-card{top:1226px;height:253px;background:var(--card);border-radius:6px;padding:26px 18px;text-align:center;font-size:15px;line-height:20px;color:#3a3f44}
.why-card h3{font-size:15px;font-weight:500;color:var(--blue);margin-bottom:20px}
.why-list{left:787px;top:1226px;width:275px;height:253px;background:var(--blue);border-radius:44px 0 44px 0;padding:22px 0 0 54px;color:var(--white);font-size:15px;list-style:none}
.why-list li{height:26.6px;display:flex;align-items:center;gap:10px}
.btn{display:flex;align-items:center;justify-content:center;font-size:15px;font-weight:500}
.btn-blue{background:var(--blue);color:var(--white)}
.btn-white{background:var(--white);color:var(--blue)}
.tier{text-align:center;font-size:13px;line-height:27px}
.tier h3{font-size:34px;font-weight:500;margin-bottom:36px}
.tier .price{font-size:26px;margin-bottom:34px}
.tier .price small{font-size:15px}
.tier b{font-weight:500}
.tier-grey{background:var(--tier);color:#2b2f33}
.tier-blue{background:var(--blue);color:var(--white);box-shadow:0 2px 8px rgba(0,0,0,.25);z-index:2}
.cert{left:148px;top:2248px;width:912px;height:276px;background:var(--blue)}
.cert h2{position:absolute;left:100px;top:38px;font-size:34px;font-weight:500;color:var(--white)}
.cert p{position:absolute;left:90px;top:114px;width:420px;text-align:center;color:var(--white);font-size:13px;line-height:20px;font-weight:500}
.foot-h{font-size:14px;font-weight:500;letter-spacing:.5px}
.links{display:grid;grid-template-columns:100px 100px;row-gap:8px;font-size:15px;color:#3a3f44}
.copy{left:0;width:1200px;text-align:center;font-size:12.5px;color:#3a3f44}
</style>
</head>
<body>

<header>
  <div class="abs" style="left:42px;top:38px">
    <div class="brand" style="font-size:40px;line-height:44px"><span class="dot"></span>BRIVOL</div>
    <div class="brand-sub">Technology Acquisition Professionals</div>
  </div>
  <nav class="abs nav">
    <a class="active" href="#">Home</a><a href="#">Events</a><a href="#">Certifications</a><a href="#">Offerings</a><a href="#">Shop</a>
  </nav>
  <div class="abs member-btn">Member area</div>
</header>

<section class="hero">
  <h1 class="abs hero-title">Promoting excellence among acquisition professionals</h1>
  <p class="abs hero-text">Learn from your peers, get answers to your daily questions, thrive in this ever-changing procurement industry.</p>
  <div class="abs join-label">JOIN US</div>
  <div class="abs join-form">
    <div class="field">Name</div>
    <div class="field">E-mail</div>
    <div class="field" style="border-bottom:0">Password
      <svg width="22" height="14" viewBox="0 0 22 14" fill="none" stroke="#9aa0a6" stroke-width="1.3"><path d="M1 7C4 2 18 2 21 7C18 12 4 12 1 7Z"/><circle cx="11" cy="7" r="3"/><path d="M4 13L18 1"/></svg>
    </div>
    <div class="submit">Sign up <svg width="8" height="10" viewBox="0 0 8 10" fill="none" stroke="#fff" stroke-width="1.5"><path d="M2 1L6 5L2 9"/></svg></div>
  </div>
  <p class="abs terms">By clicking "Sign up" I agree to our <span>Terms of Service</span>.</p>
</section>

<section class="what">
  <div class="abs band"></div>
  <h2 class="h2" style="left:152px;top:528px">What is BRIVOL?<span class="mark" style="left:55px;width:165px"></span></h2>
  <div class="abs what-text">BRIVOL is the only association serving the specialized needs of the technology acquisition professional—the person responsible for negotiating and managing contracts with suppliers of technology products and services.
    <em>Learn from your peers, get answers to your daily questions, thrive in this ever-changing procurement industry.</em></div>
</section>

<section class="mission">
  <h2 class="h2" style="left:276px;top:712px">Mission<span class="mark" style="left:0;width:70px"></span></h2>
  <p class="abs mission-lead">Our mission is to promote and support technology procurement professionals.</p>
  <p class="abs mission-text">BRIVOL works diligently to increase the effectiveness, the image and the impact of these professionals as they serve their organizations and constituents. BRIVOL works diligently to increase the effectiveness, the image and the impact of these professionals as they serve their organizations and constituents.</p>
  <div class="photo" role="img" aria-label="Portrait photo of a smiling member" style="left:615px;top:703px;width:120px;height:130px"></div>
  <div class="photo" role="img" aria-label="Portrait photo of a member in a lab coat" style="left:840px;top:627px;width:147px;height:156px;background:linear-gradient(160deg,#c9d3c8,#8e9a90)"></div>
  <div class="photo" role="img" aria-label="Portrait photo of a member with glasses" style="left:1094px;top:773px;width:106px;height:156px;background:linear-gradient(160deg,#a7a7a3,#5a3a50)"></div>
  <div class="photo" role="img" aria-label="Portrait photo of a senior member" style="left:701px;top:884px;width:139px;height:149px;background:linear-gradient(160deg,#c7a78c,#4a3a34)"></div>
  <div class="photo" role="img" aria-label="Portrait photo of a young member" style="left:920px;top:851px;width:114px;height:119px;background:linear-gradient(160deg,#c8d2d8,#6f7f8c)"></div>
  <div class="photo" role="img" aria-label="Portrait photo of a laughing member" style="left:503px;top:979px;width:83px;height:88px;background:linear-gradient(160deg,#9c7a62,#5a4a3e)"></div>
</section>

<section class="why">
  <h2 class="h2" style="left:499px;top:1155px">Why join us?<span class="mark" style="left:78px;width:73px"></span></h2>
  <div class="abs why-card" style="left:146px;width:289px">
    <h3>Share information and experiences.</h3>
    As a member, you will learn what kind of deals others are doing, obtain information about vendor ploys and practices, stay informed on best and worst deals, keep up with legislative and regulatory issues affecting your job, and much more.
  </div>
  <div class="abs why-card" style="left:460px;width:288px">
    <h3>Enhance your performance, network.</h3>
    If you're the person responsible for negotiating and managing contracts with vendors of technology products and services, BRIVOL membership is for you. It will enhance your performance and facilitate your professional growth while you network with others.
  </div>
  <ul class="abs why-list">
    <li><svg width="13" height="13" viewBox="0 0 13 13" fill="none" stroke="#fff" stroke-width="1.3"><rect x="1" y="2" width="10" height="10"/><path d="M3.5 6.5L6 9L12 1.5"/></svg>Work Smart</li>
    <li><svg width="13" height="13" viewBox="0 0 13 13" fill="none" stroke="#fff" stroke-width="1.3"><rect x="1" y="2" width="10" height="10"/><path d="M3.5 6.5L6 9L12 1.5"/></svg>Do Better Deals</li>
    <li><svg width="13" height="13" viewBox="0 0 13 13" fill="none" stroke="#fff" stroke-width="1.3"><rect x="1" y="2" width="10" height="10"/><path d="M3.5 6.5L6 9L12 1.5"/></svg>Gain valuable skills</li>
    <li><svg width="13" height="13" viewBox="0 0 13 13" fill="none" stroke="#fff" stroke-width="1.3"><rect x="1" y="2" width="10" height="10"/><path d="M3.5 6.5L6 9L12 1.5"/></svg>Advance your career</li>
    <li><svg width="13" height="13" viewBox="0 0 13 13" fill="none" stroke="#fff" stroke-width="1.3"><rect x="1" y="2" width="10" height="10"/><path d="M3.5 6.5L6 9L12 1.5"/></svg>Counter vendor ploys</li>
    <li><svg width="13" height="13" viewBox="0 0 13 13" fill="none" stroke="#fff" stroke-width="1.3"><rect x="1" y="2" width="10" height="10"/><path d="M3.5 6.5L6 9L12 1.5"/></svg>Save time and money</li>
    <li><svg width="13" height="13" viewBox="0 0 13 13" fill="none" stroke="#fff" stroke-width="1.3"><rect x="1" y="2" width="10" height="10"/><path d="M3.5 6.5L6 9L12 1.5"/></svg>Interact with your peers</li>
    <li><svg width="13" height="13" viewBox="0 0 13 13" fill="none" stroke="#fff" stroke-width="1.3"><rect x="1" y="2" width="10" height="10"/><path d="M3.5 6.5L6 9L12 1.5"/></svg>Share working solutions</li>
  </ul>
  <div class="abs btn btn-blue" style="left:491px;top:1503px;width:226px;height:39px;font-weight:400">Join us today</div>
</section>

<section class="membership">
  <h2 class="h2" style="left:147px;top:1634px">Membership<span class="mark" style="left:58px;width:92px"></span></h2>
  <div class="abs tier tier-grey" style="left:148px;top:1727px;width:299px;height:384px;padding-top:36px">
    <h3>Free</h3>
    <div class="price">$ 0 <small>/month</small></div>
    <div style="margin-top:40px"><b>50</b> videos access<br><b>50</b> support from mentor<br><b>50</b> clients data base</div>
    <div class="btn btn-blue" style="margin:24px auto 0;width:166px;height:40px">Buy now</div>
  </div>
  <div class="abs tier tier-blue" style="left:447px;top:1714px;width:356px;height:406px;padding-top:48px">
    <h3>Standard</h3>
    <div class="price">$ 50 <small>/month</small></div>
    <div style="margin-top:6px"><b>100 videos access<br>100 support from mentor<br>100 clients data base</b></div>
    <div class="btn btn-white" style="margin:48px auto 0;width:166px;height:40px">Buy now</div>
  </div>
  <div class="abs tier tier-grey" style="left:803px;top:1727px;width:257px;height:384px;padding-top:32px">
    <h3>Plus</h3>
    <div class="price">$ 100 <small>/month</small></div>
    <div style="margin-top:14px"><b>Unlimited</b> videos access<br><b>Unlimited</b> support from mentor<br><b>Unlimited</b> clients data base</div>
    <div class="btn btn-blue" style="margin:34px auto 0;width:166px;height:40px">Buy now</div>
  </div>
</section>

<section class="abs cert">
  <h2>Get Professionally Certified</h2>
  <p>BRIVOL Certification programs are designed to elevate professional standards, enhance individual performance and identify those who demonstrate knowledge essential to the practice of competent technology procurement.</p>
  <div class="abs btn btn-white" style="left:191px;top:209px;width:227px;height:40px;font-weight:400">Get certified</div>
</section>
<div class="abs" role="img" aria-label="Photo of a smiling businesswoman presenting with an open hand" style="left:700px;top:2185px;width:330px;height:339px;background:linear-gradient(180deg,#7d7f88,#5b5e68);border-radius:140px 140px 0 0"></div>
<div class="abs" role="img" aria-label="Certification badge" style="left:688px;top:2197px;width:100px;height:100px;border-radius:50%;background:var(--white);border:6px solid var(--blue-dark)"></div>

<footer>
  <div class="abs" style="left:148px;top:2666px">
    <div class="brand-sub" style="font-size:15px">Association of</div>
    <div class="brand" style="font-size:50px;line-height:54px"><span class="dot"></span>BRIVOL</div>
    <div class="brand-sub" style="font-size:15px">Technology Acquisition Professionals</div>
  </div>
  <div class="abs foot-h" style="left:605px;top:2668px">QUICK LINKS</div>
  <div class="abs links" style="left:571px;top:2698px">
    <span>Home</span><span>Certifications</span><span>Events</span><span>Shop</span><span>Offerings</span><span>Member area</span>
  </div>
  <div class="abs foot-h" style="left:979px;top:2668px">FOLLOW US</div>
  <svg class="abs" style="left:980px;top:2696px" width="82" height="20" viewBox="0 0 82 20" fill="none" stroke="#3a3f44" stroke-width="1.4">
    <circle cx="9" cy="10" r="8"/><circle cx="41" cy="10" r="8"/><circle cx="73" cy="10" r="8"/>
  </svg>
  <p class="abs copy" style="top:2820px">© COPYRIGHT 2019 BRIVOL ASSOCIATION OF TECHNOLOGY ACQUISITION PROFESSIONALS</p>
  <p class="abs copy" style="top:2850px">Helping The World Procurement Community Do Better Deals For 45 Years!</p>
  <p class="abs copy" style="top:2878px">USA 555-014-2290</p>
</footer>

</body>
</html>
```